Messianic Prophetic Timeline

I would like to create a timeline that will fit on a horizontal 11 x 8 1/2 (8 1/2 x11) sheet of paper.
I have two images that will need to be merged.
There should be 7 time points. 1) 457BCE-26 AD, 2) 26 AD-30AD, 3) 30 AD-66 AD, 4) 66AD- 70AD 5) 70 AD, 6) 70AD-20??, and 7) Future
The #6 and #7 from each graphic should be merged. The 30AD-70AD can be dropped. Time point #7 Future has two different texts both need to be preserved, I would like time point #7 to be larger than the other time points.
There are scripture verses that are associated with each block that should be preserved and be more prominent.
These images are from a powerpoint slide, but I want something that can be printed out.
I run a website www.brightcoverstudy.org. I have some brand colors that if can be incorporated or at least have some color cohesion would be great, but that is not as important as readability.
Background images are nice - The idea is one of conflict between light and darkness, two opposing forces, Christ and anti-Christ. Maybe a king on a white horse battling a large serpent dragon
If you can incorporate this quote near timeblock #1-2 "From the decree to restore Jerusalem until Messiah 483 year"
Second quote anywhere "He will make a covenant with many for 7 years"

```html
<!DOCTYPE html>
<html lang="en">
<head>
<meta charset="utf-8">
<title>Jesus and Daniel Chronology</title>
<link href="https://fonts.googleapis.com/css2?family=Bebas+Neue&family=Roboto+Condensed:wght@700&family=Roboto:ital,wght@0,400;0,700;1,400;1,700&display=swap" rel="stylesheet">
<style>
  :root {
    --backdrop: #85868a;
    --teal: #0f847e;
    --teal-deep: #066361;
    --teal-light: #84d3cf;
    --road-light: #f5f6f7;
    --road-dark: #d6d7da;
    --white: #ffffff;
  }
  * { margin: 0; padding: 0; box-sizing: border-box; }
  html, body { width: 1200px; height: 988px; overflow: hidden; background: var(--backdrop); }
  body { position: relative; font-family: "Roboto", Arial, sans-serif; color: var(--white); }

  .sheet {
    position: absolute; left: 100px; top: 107px; width: 1001px; height: 774px; overflow: hidden;
    background: radial-gradient(ellipse at 55% 50%, #1a9a92 0%, var(--teal) 45%, var(--teal-deep) 100%);
  }
  .artwork-backdrop {
    position: absolute; left: 250px; top: 90px; width: 560px; height: 560px; border-radius: 50%;
    background: radial-gradient(circle, rgba(255,255,255,0.07) 0%, rgba(255,255,255,0) 70%);
  }
  .road { position: absolute; left: 0; top: 0; width: 1001px; height: 774px; }

  .el { position: absolute; white-space: nowrap; }
  .heading { font-family: "Roboto Condensed", "Arial Narrow", sans-serif; font-weight: 700; text-align: right; line-height: 1; }
  .heading .big { display: block; font-size: 26px; letter-spacing: -0.6px; transform: scaleY(1.12); transform-origin: top; }
  .heading .sub { display: block; font-size: 14px; margin-top: 6px; }
  .note { font-weight: 700; font-size: 14px; line-height: 15px; }
  .ref { font-style: italic; font-size: 12px; line-height: 17px; font-weight: 400; }
  .date { font-weight: 700; font-size: 16px; }

  .title {
    left: 322px; top: 44px; font-family: "Bebas Neue", "Arial Narrow", sans-serif; font-size: 66px; line-height: 1;
    text-shadow: 0 2px 6px rgba(0,0,0,0.25);
  }
  .title .accent { color: var(--teal-light); }

  .brand { left: 640px; top: 136px; display: flex; align-items: center; gap: 10px; font-size: 26px; font-weight: 400; }
  .brand .dot { width: 22px; height: 22px; border-radius: 50%; background: var(--white); }

  .decree-box {
    position: absolute; left: 0; top: 178px; width: 212px; height: 80px;
    background: rgba(26,160,150,0.85); display: flex; align-items: center; justify-content: center;
    text-align: center; font-style: italic; font-size: 15px; line-height: 20px;
  }
  .covenant-quote { left: 28px; top: 645px; font-style: italic; font-size: 17px; }
  .future { left: 774px; top: 642px; font-weight: 700; font-size: 30px; letter-spacing: -0.5px; }
  .url-band {
    position: absolute; left: 160px; top: 703px; width: 390px; height: 50px;
    background: radial-gradient(ellipse at center, rgba(30,190,180,0.8) 0%, rgba(30,190,180,0) 72%);
  }
  .url { left: 193px; top: 715px; font-size: 21px; font-weight: 700; letter-spacing: 3.2px; }
</style>
</head>
<body>
<main class="sheet">
  <div class="artwork-backdrop" role="img" aria-label="Faint background artwork of a rider on a white horse"></div>

  <svg class="road" viewBox="175 188 1760 1360" aria-hidden="true">
    <defs>
      <linearGradient id="road-fill" x1="0" y1="0" x2="1" y2="1">
        <stop offset="0" stop-color="var(--road-light)"/>
        <stop offset="1" stop-color="var(--road-dark)"/>
      </linearGradient>
      <g id="marker">
        <ellipse cx="10" cy="32" rx="54" ry="24" fill="#aab3b7" opacity="0.7"/>
        <path d="M-50,0 v30 a50,20 0 0 0 100,0 v-30 z" fill="#139782"/>
        <ellipse cx="0" cy="0" rx="50" ry="20" fill="#36c3b8"/>
        <ellipse cx="0" cy="2" rx="28" ry="10" fill="#13998f"/>
      </g>
    </defs>
    <path d="M175,456 C350,462 540,472 535,487 C528,500 330,502 250,512" fill="none" stroke="var(--road-light)" stroke-width="9" stroke-linecap="round"/>
    <path fill="url(#road-fill)" d="
      M550,546 C680,556 768,570 773,590
      C778,612 640,628 520,640
      C440,648 380,652 392,668
      C400,682 520,692 700,705
      C900,722 1150,770 1270,805
      C1345,828 1350,860 1320,890
      C1270,935 1100,975 950,1020
      C830,1055 785,1070 797,1095
      C815,1130 930,1165 1060,1200
      C1300,1262 1650,1320 1935,1372
      L1935,1548 L1905,1548
      C1600,1470 1200,1400 900,1320
      C720,1265 620,1210 612,1140
      C605,1070 700,1020 840,965
      C960,918 1120,880 1170,845
      C1185,815 1120,795 980,782
      C780,762 520,735 380,714
      C300,702 275,690 280,670
      C285,645 380,620 500,610
      C600,602 668,603 668,594
      C668,578 610,568 550,566 Z"/>
    <g fill="none" stroke="var(--white)" stroke-width="2">
      <path d="M440,268 V398 H374 V455"/>
      <path d="M825,460 V548 H578 V612"/>
      <path d="M453,850 V683 H682 V717"/>
      <path d="M1248,622 H1032 V756"/>
      <path d="M1583,648 V832 H1110 V912"/>
      <path d="M466,1235 V1040 H846 V1165"/>
      <path d="M1425,1028 V1320"/>
    </g>
    <use href="#marker" transform="translate(376,460) scale(0.36)"/>
    <use href="#marker" transform="translate(578,618) scale(0.4)"/>
    <use href="#marker" transform="translate(683,725) scale(0.48)"/>
    <use href="#marker" transform="translate(1033,762) scale(0.6)"/>
    <use href="#marker" transform="translate(1110,915) scale(0.85)"/>
    <use href="#marker" transform="translate(846,1160) scale(1.15)"/>
    <use href="#marker" transform="translate(1424,1315) scale(1.75)"/>
  </svg>

  <h1 class="el title">JESUS AND DANIEL <span class="accent">CHRONOLOGY</span></h1>
  <div class="el brand"><span class="dot"></span>Lampstand Notes</div>

  <div class="decree-box">From the decree to<br>restore Jerusalem until<br>Messiah 483 year</div>

  <!-- Messiah -->
  <div class="el heading" style="right:860px; top:52px;"><span class="big">MESIAH</span><span class="sub">Cut Off</span></div>
  <div class="el note" style="left:163px; top:50px;">438 Years<br>From Decree</div>
  <div class="el ref" style="left:163px; top:86px;">Dan 9:26 Ezra 7,9:9</div>
  <div class="el date" style="left:120px; top:125px;">457 BCE - 26 AD</div>

  <!-- Covenant made -->
  <div class="el heading" style="right:639px; top:149px;"><span class="big">COVENANT</span><span class="sub">Made</span></div>
  <div class="el note" style="left:381px; top:150px;">Jesus Make Covenant with<br>many, stops Sacrifice</div>
  <div class="el ref" style="left:381px; top:185px;">Dan 9:27</div>
  <div class="el date" style="left:226px; top:182px;">26 AD - 30AD</div>

  <!-- Apostles -->
  <div class="el date" style="left:218px; top:260px;">30 AD - 66 AD</div>
  <div class="el heading" style="right:856px; top:325px;"><span class="big">APOSTLES</span><span class="sub">Persecution</span></div>
  <div class="el note" style="left:168px; top:328px;">In Synagogue By family,<br>friends By Kings</div>
  <div class="el ref" style="left:168px; top:364px;">Luke 21:12-19</div>

  <!-- Vengeance -->
  <div class="el heading" style="right:523px; top:249px;"><span class="big">VENGEANCE</span><span class="sub">Days of</span></div>
  <div class="el note" style="left:496px; top:253px;">Jerusalem<br>Surrounded Flee</div>
  <div class="el ref" style="left:496px; top:285px;">Luke 21:20-23</div>
  <div class="el date" style="left:516px; top:312px;">66 AD - 70 AD</div>

  <!-- Jerusalem -->
  <div class="el heading" style="right:205px; top:262px;"><span class="big">JERUSALEM</span><span class="sub">Desolation</span></div>
  <div class="el note" style="left:808px; top:267px;">Dispersed In<br>Nations</div>
  <div class="el ref" style="left:808px; top:310px;">Luke 21:24<br>Is 61:2<br>Hos 9:7</div>
  <div class="el date" style="left:461px; top:376px;">70 AD</div>

  <!-- Gentiles -->
  <div class="el heading" style="right:846px; top:502px;"><span class="big">GENTILES</span><span class="sub">Time of</span></div>
  <div class="el note" style="left:174px; top:502px;">Trample<br>Jerusalem</div>
  <div class="el ref" style="left:174px; top:551px;">Lk 21:8-11,24<br>Mat 24:4-14</div>
  <div class="el date" style="left:386px; top:503px; font-size:23px;">70 AD - 20??</div>

  <!-- Covenant future -->
  <div class="el heading" style="right:298px; top:502px;"><span class="big">COVENANT</span><span class="sub">Made</span></div>
  <div class="el" style="left:724px; top:498px; font-size:15px;">Stops Sacrifice Causes</div>
  <div class="el note" style="left:724px; top:521px; font-size:15px;">Abomination of Desolation</div>
  <div class="el ref" style="left:724px; top:551px; font-size:13px; line-height:20px;">Luke 21:25+&nbsp;&nbsp;&nbsp;Matt 24:15<br>Dan 9:27, 11:31, 12:11</div>
  <div class="el future">FUTURE</div>

  <p class="el covenant-quote">He will make a covenant with many for 7 years</p>

  <div class="url-band"></div>
  <div class="el url">www.brightcoverstudy.org</div>
</main>
</body>
</html>
```